Gym Membership Sales Sheet

I want this sheet to showcase the four contract types of bronze, silver, 6 month and platinum underneath of the three membership types of individual, partner and family. I am not particularly stuck on the bronze, silver, gold, platinum structure if you feel you have four better names that would work. However on the new sheet I want to remove the option for a 6 month contract. So, move up the PIF for just one year option and remove the three month option. Then remove everything else on the page. Add in hydromassage/tanning in with silver, gold and platinum contracts. The sheet needs to be simple.

Three membership types of individual, partner and family.

Then Bronze, silver, gold, platinum.

Silver, Gold and platinum members get hydromassage and tanning access. Only gold and platinum members get 15% of personal training and kinetics programs. Gold and Platinum members get free kid zone access as well.

Target Market(s)

Families, women and young adult males

Industry/Entity Type

Fitness

Colors
9bcb3c

Requirements
Must have
• Must have a cohesive design that highlights the membership types effectively. A design that is simple yet effective in causing people to choose Gold and Platinum plans. The goal of it is to up sell everyone into Gold and Platinum memberships.
Nice to have
• It would be nice to have three design types. One that appeals to women. One that appeals to young adult males and the third that appeals to families.
Should not have
• It should not be over complex and should not have a 6 month membership or 3 month membership options.

```html
<!DOCTYPE html>
<html lang="en">
<head>
<meta charset="utf-8">
<title>Membership Rates</title>
<link rel="stylesheet" href="https://fonts.googleapis.com/css2?family=Oswald:wght@500;700&family=Open+Sans:wght@400;600;700&display=swap">
<style>
  :root {
    --green: #6fa83a;
    --green-light: #9bcb3c;
    --green-pale: #e8f2d8;
    --dark: #2a2c2b;
    --grey: #d9dcd6;
    --grey-light: #f1f2ef;
    --text: #3a3a3a;
    --white: #ffffff;
  }
  * { box-sizing: border-box; margin: 0; padding: 0; }
  html, body { width: 851px; height: 1200px; overflow: hidden; background: var(--white); }
  body { font-family: "Open Sans", Arial, sans-serif; color: var(--text); position: relative; }

  .sheet-label { position: absolute; left: 40px; top: 26px; font-size: 12px; font-weight: 700; }
  .title-band { position: absolute; top: 50px; right: 0; width: 520px; height: 70px; }
  .title-band svg { position: absolute; inset: 0; }
  .title-band h1 {
    position: absolute; right: 40px; top: 12px;
    font-family: "Oswald", Arial, sans-serif; font-weight: 700; font-size: 38px;
    color: var(--white); letter-spacing: 1px;
  }
  .offer-line { position: absolute; left: 40px; right: 40px; top: 136px; font-size: 13px; font-weight: 600; text-align: center; }
  .fee-bar {
    position: absolute; left: 40px; right: 40px; top: 164px; height: 40px;
    background: var(--dark); color: var(--white); text-align: center;
    font-family: "Oswald", Arial, sans-serif; font-weight: 500; font-size: 22px; line-height: 40px;
  }

  .rates-table { position: absolute; left: 36px; top: 212px; width: 779px; border-collapse: separate; border-spacing: 4px; }
  .rates-table th {
    font-family: "Oswald", Arial, sans-serif; font-weight: 700; font-size: 20px; color: var(--dark);
    height: 34px; background: var(--grey-light);
  }
  .rates-table th.corner { background: transparent; }
  .rates-table td { height: 78px; text-align: center; font-size: 13px; background: var(--grey-light); }
  .rates-table td.tier {
    width: 130px; background: var(--green); color: var(--white);
    font-family: "Oswald", Arial, sans-serif; font-weight: 700; font-size: 20px;
  }
  .rates-table tr.term td { height: 46px; background: var(--grey); font-weight: 600; }
  .rates-table tr.term td.tier { font-size: 16px; background: var(--dark); color: var(--white); }
  .rates-table tr.featured td:not(.tier) { background: var(--green-pale); }
  .price { display: block; font-family: "Oswald", Arial, sans-serif; font-weight: 700; font-size: 22px; color: var(--green); }
  .perk { display: block; font-size: 11px; margin-top: 2px; }

  .promo { position: absolute; top: 656px; height: 66px; background: var(--green); color: var(--white);
    font-family: "Oswald", Arial, sans-serif; font-weight: 700; font-size: 20px; line-height: 1.2;
    display: flex; align-items: center; justify-content: center; text-align: center; padding: 0 28px; }
  .promo-left { left: 40px; width: 370px; clip-path: polygon(0 0, 100% 0, 94% 100%, 0 100%); }
  .promo-right { left: 420px; width: 391px; clip-path: polygon(6% 0, 100% 0, 100% 100%, 0 100%); }

  .perk-list { position: absolute; left: 40px; top: 746px; width: 370px; }
  .perk-list h2 { font-family: "Oswald", Arial, sans-serif; font-size: 17px; color: var(--dark); margin-bottom: 8px; }
  .perk-list li { list-style: none; font-size: 13px; padding: 6px 10px; background: var(--grey-light); margin-bottom: 4px; }

  .addons { position: absolute; left: 440px; top: 746px; width: 371px; border: 2px solid var(--dark); }
  .addons h2 { background: var(--dark); color: var(--white); font-family: "Oswald", Arial, sans-serif;
    font-size: 17px; text-align: center; padding: 6px 0; }
  .addons li { list-style: none; display: flex; justify-content: space-between; font-size: 13px; padding: 6px 14px; }
  .addons li b { color: var(--green); }

  .brand { position: absolute; right: 40px; top: 1000px; display: flex; align-items: center; gap: 10px; }
  .brand-mark { width: 26px; height: 26px; background: var(--green); }
  .brand-name { font-family: "Oswald", Arial, sans-serif; font-weight: 700; font-size: 36px; color: var(--dark); }

  .footer-band { position: absolute; left: 0; bottom: 0; width: 851px; height: 80px; }
</style>
</head>
<body>
  <p class="sheet-label">Membership Structure</p>

  <header class="title-band">
    <svg width="520" height="70" viewBox="0 0 520 70" aria-hidden="true">
      <polygon points="0,0 70,0 50,70 0,70" fill="var(--dark)"/>
      <polygon points="80,0 520,0 520,70 60,70" fill="var(--green)"/>
    </svg>
    <h1>MEMBERSHIP RATES</h1>
  </header>

  <p class="offer-line">Offer valid for new members who join or renew this month with bonus perks included</p>
  <div class="fee-bar">All Memberships Have A $49 Initial Enrollment Fee</div>

  <table class="rates-table">
    <tr>
      <th class="corner"></th><th>INDIVIDUAL</th><th>PARTNER</th><th>FAMILY</th>
    </tr>
    <tr class="term">
      <td class="tier">Memberships</td><td>12 Month / Paid In Full</td><td>12 Month / Paid In Full</td><td>12 Month / Paid In Full</td>
    </tr>
    <tr>
      <td class="tier">Bronze</td>
      <td><span class="price">$19.99</span><span class="perk">Gym access</span></td>
      <td><span class="price">$34.99</span><span class="perk">Gym access</span></td>
      <td><span class="price">$49.99</span><span class="perk">Gym access</span></td>
    </tr>
    <tr>
      <td class="tier">Silver</td>
      <td><span class="price">$29.99</span><span class="perk">Hydromassage / Tanning</span></td>
      <td><span class="price">$49.99</span><span class="perk">Hydromassage / Tanning</span></td>
      <td><span class="price">$69.99</span><span class="perk">Hydromassage / Tanning</span></td>
    </tr>
    <tr class="featured">
      <td class="tier">Gold</td>
      <td><span class="price">$39.99</span><span class="perk">Hydromassage / Tanning · Kid Zone</span></td>
      <td><span class="price">$64.99</span><span class="perk">Hydromassage / Tanning · Kid Zone</span></td>
      <td><span class="price">$89.99</span><span class="perk">Hydromassage / Tanning · Kid Zone</span></td>
    </tr>
    <tr class="featured">
      <td class="tier">Platinum</td>
      <td><span class="price">$49.99</span><span class="perk">Hydromassage / Tanning · Kid Zone</span></td>
      <td><span class="price">$79.99</span><span class="perk">Hydromassage / Tanning · Kid Zone</span></td>
      <td><span class="price">$109.99</span><span class="perk">Hydromassage / Tanning · Kid Zone</span></td>
    </tr>
  </table>

  <div class="promo promo-left">Only Gold And Platinum Members</div>
  <div class="promo promo-right">Get 15% Off Personal Training And Kinetics Programs</div>

  <section class="perk-list">
    <h2>Gold &amp; Platinum Perks</h2>
    <ul>
      <li>Free Kid Zone access</li>
      <li>Hydromassage and tanning</li>
      <li>15% off personal training</li>
      <li>15% off kinetics programs</li>
      <li>Unlimited group classes</li>
    </ul>
  </section>

  <section class="addons">
    <h2>Additional Membership</h2>
    <ul>
      <li>Add a child <b>$10</b></li>
      <li>Add a spouse <b>$20</b></li>
      <li>Guest day pass <b>$10</b></li>
      <li>Tanning single session <b>$8</b></li>
      <li>Hydromassage session <b>$8</b></li>
    </ul>
  </section>

  <div class="brand">
    <span class="brand-mark"></span>
    <span class="brand-name">KORVATH FITNESS</span>
  </div>

  <svg class="footer-band" viewBox="0 0 851 80" aria-hidden="true">
    <polygon points="0,30 851,0 851,80 0,80" fill="var(--dark)"/>
    <polygon points="0,20 560,0 600,0 0,36" fill="var(--green)"/>
  </svg>
</body>
</html>
```